Business card design needed

Design:
Want the logo/design to have an enviromental feel
Simple look not to busy

Company Info:
Pre purchase building and pest inspections
Registered building practitoner DB-U 58147 (please include building commission logo in design)

Industry/Entity Type

Building

Contact Information for Business Card

Company name:
Fernvale Building and Pest inspections

Inspectors:
Dean Harker 0451 278 914
Greg Sutcliffe 0419 562 843
Email: fernvalebpi@mailpost.example

```html
<!DOCTYPE html>
<html lang="en">
<head>
<meta charset="utf-8">
<title>Fernvale Building and Pest inspections – Business Card</title>
<link rel="stylesheet" href="https://fonts.googleapis.com/css2?family=Josefin+Sans:wght@400;700&display=swap">
<style>
  :root {
    --backdrop: #e8e4dd;
    --card-dark: #1f1f20;
    --card-dark-mid: #2c2c2d;
    --band-line: #3a3a3b;
    --card-light: #ffffff;
    --eco-green: #8fd11b;
    --ink: #111111;
    --rule-grey: #888888;
    --bar-black: #0c0c0c;
    --seal: #b59a2a;
  }
  * { box-sizing: border-box; margin: 0; padding: 0; }
  html, body {
    width: 1200px; height: 1000px; overflow: hidden;
    background: var(--backdrop);
    font-family: "Josefin Sans", sans-serif;
  }
  .canvas { position: relative; width: 1200px; height: 1000px; }

  .card { position: absolute; left: 252px; width: 689px; height: 398px; overflow: hidden; }

  /* Front */
  .card-front {
    top: 82px;
    background: radial-gradient(ellipse at 50% 35%, var(--card-dark-mid) 0%, var(--card-dark) 70%);
  }
  .front-band {
    position: absolute; left: 0; right: 0; top: 78px; height: 238px;
    border-top: 2px solid var(--band-line);
    border-bottom: 2px solid var(--band-line);
  }
  .front-brand {
    position: absolute; left: 0; right: 0; top: 172px;
    text-align: center; color: var(--eco-green); font-weight: 700;
  }
  .front-brand .brand-mark {
    display: inline-block; width: 34px; height: 34px; border-radius: 50%;
    background: var(--eco-green); margin-bottom: 18px;
  }
  .front-brand .brand-name { font-size: 44px; line-height: 1; letter-spacing: 0.5px; }
  .front-brand .brand-sub { font-size: 15px; letter-spacing: 3px; text-transform: uppercase; margin-top: 6px; }
  .authority-badge {
    position: absolute; right: 22px; bottom: 20px;
    width: 42px; height: 42px; border-radius: 50%;
    border: 3px solid var(--seal);
  }

  /* Back */
  .card-back { top: 552px; background: var(--card-light); }
  .back-brand {
    position: absolute; left: 58px; top: 40px;
    color: var(--eco-green); font-weight: 700;
  }
  .back-brand .brand-mark {
    display: block; width: 26px; height: 26px; border-radius: 50%;
    background: var(--eco-green); margin: 0 0 44px 4px;
  }
  .back-brand .brand-name { font-size: 34px; line-height: 1; }
  .back-brand .brand-sub { font-size: 12px; letter-spacing: 2.4px; text-transform: uppercase; margin-top: 5px; }

  .inspectors { position: absolute; left: 68px; top: 238px; color: var(--ink); }
  .inspectors .label { color: var(--eco-green); font-size: 14px; margin-bottom: 6px; }
  .inspectors .person { font-size: 18px; line-height: 27px; }
  .inspectors .email { font-size: 12px; margin-top: 5px; }
  .inspectors .email em { font-style: normal; color: var(--eco-green); }

  .divider { position: absolute; left: 314px; top: 238px; width: 1px; height: 92px; background: var(--rule-grey); }
  .registration { position: absolute; left: 331px; top: 276px; font-size: 15px; color: var(--ink); }
  .registration span { color: var(--eco-green); }

  .bar-black { position: absolute; left: 0; top: 381px; width: 525px; height: 17px; background: var(--bar-black); }
  .bar-green { position: absolute; left: 531px; top: 381px; width: 158px; height: 17px; background: var(--eco-green); }
</style>
</head>
<body>
<main class="canvas">
  <section class="card card-front" aria-label="Business card front">
    <div class="front-band"></div>
    <div class="front-brand">
      <span class="brand-mark"></span>
      <div class="brand-name">Fernvale Building</div>
      <div class="brand-sub">and Pest inspections</div>
    </div>
    <div class="authority-badge" role="img" aria-label="Registration authority seal"></div>
  </section>

  <section class="card card-back" aria-label="Business card back">
    <div class="back-brand">
      <span class="brand-mark"></span>
      <div class="brand-name">Fernvale Building</div>
      <div class="brand-sub">and Pest inspections</div>
    </div>
    <div class="inspectors">
      <p class="label">Inspectors:</p>
      <p class="person">Dean Harker - 0451 278 914</p>
      <p class="person">Greg Sutcliffe - 0419 562 843</p>
      <p class="email">Email: <em>fernvale</em>bpi@mailpost.example</p>
    </div>
    <div class="divider"></div>
    <p class="registration">Registered building practitoner <span>DB-U 58147</span></p>
    <div class="bar-black"></div>
    <div class="bar-green"></div>
  </section>
</main>
</body>
</html>
```